Business card for communications

Need a business card for my consulting business - I work with not for profits, start ups and social enterprises on their media, communications campaigns.

Please see my website for colours, images and fonts www.morvenquillet.example

Morven Quillet
Communications & Campaign strategist
Sydney - Melbourne
M: 0498 317 250
E: morven@morvenquillet.example
S: morvenquillet
W: morvenquillet.example
T: @morvenquillet

(above is info only and can be presented any way e.g. should not have to be M for mobile - it should be an icon)
Updates

Dear designers I have updated the brief and uploaded high res images from my website for you to use. The designs so far with the use of images and icons are much better so far. Thank you I look forward to receiving your revised designs. Morven Quillet

Industry/Entity Type

Communications

Font styles to use
Sans Serif

Requirements
Must have
• Icons for contact details
Images from the website www.morvenquillet.example
Nice to have
• Images - attached

```html
<!DOCTYPE html>
<html lang="en">
<head>
<meta charset="utf-8">
<title>Morven Quillet – Business Card</title>
<link rel="stylesheet" href="https://fonts.googleapis.com/css2?family=Arimo:wght@400;700&display=swap">
<style>
  :root {
    --ink: #0b0b0b;
    --card-black: #050505;
    --accent: #fad40c;
    --white: #ffffff;
    --paper: #e9e7e3;
    --icon-fill: #f3e08a;
  }
  * { box-sizing: border-box; margin: 0; padding: 0; }
  html, body {
    width: 1200px; height: 848px; overflow: hidden;
    background: var(--paper);
    font-family: "Arimo", Arial, sans-serif;
  }
  .stage {
    width: 1200px; height: 848px;
    display: flex; align-items: center; justify-content: center; gap: 30px;
  }
  .card {
    position: relative; width: 555px; height: 338px; overflow: hidden;
    box-shadow: 0 10px 28px rgba(0,0,0,.22);
  }

  /* Front */
  .card--front { background: var(--card-black); }
  .front__name {
    position: absolute; left: 28px; top: 152px; width: 250px;
    color: var(--accent); font-size: 26px; letter-spacing: .3px; font-weight: 400;
    white-space: nowrap;
  }
  .front__divider {
    position: absolute; left: 288px; top: 38px; width: 2px; height: 204px;
    background: var(--white);
  }
  .contacts {
    position: absolute; left: 306px; top: 48px; right: 12px; list-style: none;
  }
  .contacts__item {
    display: flex; align-items: center; gap: 12px; height: 30px;
    color: var(--white); font-size: 13px; white-space: nowrap;
  }
  .contacts__icon { width: 23px; height: 23px; flex: none; }
  .front__stripe-white {
    position: absolute; left: 0; right: 0; top: 262px; height: 7px; background: var(--white);
  }
  .front__band {
    position: absolute; left: 0; right: 0; top: 273px; bottom: 0; background: var(--accent);
  }

  /* Back */
  .card--back { background: var(--accent); }
  .back__heading {
    position: absolute; left: 0; right: 0; top: 58px; text-align: center;
    font-size: 26px; font-weight: 400; color: var(--ink); letter-spacing: .5px;
  }
  .back__heading .plus { font-weight: 700; margin-right: 10px; }
  .services {
    position: absolute; left: 22px; right: 22px; top: 140px;
    display: flex; justify-content: space-between; list-style: none;
  }
  .service {
    width: 118px; display: flex; flex-direction: column; align-items: center;
    text-align: center; color: var(--ink);
  }
  .service__icon { width: 84px; height: 84px; margin-bottom: 16px; }
  .service__label { font-size: 15px; line-height: 1.1; }
  .service__label--caps { text-transform: uppercase; font-size: 13px; }
</style>
</head>
<body>
<main class="stage">

  <section class="card card--front" aria-label="Card front">
    <h1 class="front__name">MORVEN QUILLET</h1>
    <div class="front__divider"></div>
    <ul class="contacts">
      <li class="contacts__item">
        <svg class="contacts__icon" viewBox="0 0 24 24" aria-hidden="true"><rect width="24" height="24" rx="5" fill="#fad40c"/><path d="M12 5a5 5 0 0 0-5 5c0 3.5 5 9 5 9s5-5.5 5-9a5 5 0 0 0-5-5zm0 7a2 2 0 1 1 0-4 2 2 0 0 1 0 4z" fill="#fff"/></svg>
        <span>Sydney - Melbourne</span>
      </li>
      <li class="contacts__item">
        <svg class="contacts__icon" viewBox="0 0 24 24" aria-hidden="true"><rect width="24" height="24" rx="5" fill="#fad40c"/><rect x="8" y="4.5" width="8" height="15" rx="1.5" fill="none" stroke="#fff" stroke-width="1.6"/><circle cx="12" cy="17" r="1" fill="#fff"/></svg>
        <span>0498 317 250</span>
      </li>
      <li class="contacts__item">
        <svg class="contacts__icon" viewBox="0 0 24 24" aria-hidden="true"><rect width="24" height="24" rx="5" fill="#fad40c"/><rect x="5" y="7" width="14" height="10" fill="none" stroke="#fff" stroke-width="1.6"/><path d="M5 7l7 6 7-6" fill="none" stroke="#fff" stroke-width="1.6"/></svg>
        <span>morven@morvenquillet.example</span>
      </li>
      <li class="contacts__item">
        <svg class="contacts__icon" viewBox="0 0 24 24" aria-hidden="true"><rect width="24" height="24" rx="5" fill="#fad40c"/><circle cx="12" cy="12" r="5.5" fill="#fff"/></svg>
        <span>morvenquillet</span>
      </li>
      <li class="contacts__item">
        <svg class="contacts__icon" viewBox="0 0 24 24" aria-hidden="true"><rect width="24" height="24" rx="5" fill="#fad40c"/><circle cx="12" cy="12" r="6.5" fill="none" stroke="#fff" stroke-width="1.5"/><path d="M5.5 12h13M12 5.5c-3 3.5-3 9.5 0 13M12 5.5c3 3.5 3 9.5 0 13" fill="none" stroke="#fff" stroke-width="1.2"/></svg>
        <span>morvenquillet.example</span>
      </li>
      <li class="contacts__item">
        <svg class="contacts__icon" viewBox="0 0 24 24" aria-hidden="true"><rect width="24" height="24" rx="5" fill="#fad40c"/><rect x="7" y="7" width="10" height="10" fill="#fff"/></svg>
        <span>@morvenquillet</span>
      </li>
    </ul>
    <div class="front__stripe-white"></div>
    <div class="front__band"></div>
  </section>

  <section class="card card--back" aria-label="Card back">
    <h2 class="back__heading"><span class="plus">+</span>SERVICES</h2>
    <ul class="services">
      <li class="service">
        <svg class="service__icon" viewBox="0 0 84 84" role="img" aria-label="Pencil and ruler icon"><circle cx="42" cy="42" r="40" fill="#fff"/><circle cx="42" cy="42" r="24" fill="#f3e08a"/></svg>
        <span class="service__label">Communications Strategy</span>
      </li>
      <li class="service">
        <svg class="service__icon" viewBox="0 0 84 84" role="img" aria-label="Typewriter icon"><circle cx="42" cy="42" r="40" fill="#fff"/><circle cx="42" cy="42" r="24" fill="#f3e08a"/></svg>
        <span class="service__label">Media Relations</span>
      </li>
      <li class="service">
        <svg class="service__icon" viewBox="0 0 84 84" role="img" aria-label="Stacked folders icon"><circle cx="42" cy="42" r="40" fill="#fff"/><circle cx="42" cy="42" r="24" fill="#f3e08a"/></svg>
        <span class="service__label service__label--caps">PR &amp;<br>Campaigns</span>
      </li>
      <li class="service">
        <svg class="service__icon" viewBox="0 0 84 84" role="img" aria-label="Light bulb icon"><circle cx="42" cy="42" r="40" fill="#fff"/><circle cx="42" cy="42" r="24" fill="#f3e08a"/></svg>
        <span class="service__label service__label--caps">Strategic<br>Counsel</span>
      </li>
    </ul>
  </section>

</main>
</body>
</html>
```